Veltrona stationery design

Design stationery for us that fits with the colours of the logo. We are looking for letterheads, business cards etc. Something we can use for a prospectus and marketing presentations in power point. Must be completed in such a manner that it represents a corporate image for large enterprise clients and other large organisations. The company is a project assurance and monitoring company that works in all industries.

```html
<!DOCTYPE html>
<html lang="en">
<head>
<meta charset="utf-8">
<title>Veltrona Stationery</title>
<link href="https://fonts.googleapis.com/css2?family=Montserrat:wght@400;500;600;700;800&display=swap" rel="stylesheet">
<style>
:root{
  --navy:#1c3f73;
  --navy-dark:#17355f;
  --orange:#f26a1f;
  --paper:#f8f8f6;
  --ink:#1f2a3a;
  --muted:#5a6472;
  --bg:#dcdcdc;
}
*{box-sizing:border-box;margin:0;padding:0}
html,body{width:1200px;height:800px;overflow:hidden}
body{background:var(--bg);font-family:"Montserrat",sans-serif;color:var(--ink);position:relative}
.piece{position:absolute;background:var(--paper);overflow:hidden;box-shadow:0 2px 6px rgba(0,0,0,.18)}
.corner{position:absolute;right:0;bottom:0}
.brand{display:flex;align-items:center;gap:5px;font-weight:700;color:var(--navy);letter-spacing:.02em;white-space:nowrap}
.brand .mark{background:var(--orange);flex:none}
.brand.light{color:#fff}
.contact{list-style:none;font-size:5px;line-height:1.5;color:var(--ink)}
.contact li{display:flex;gap:5px;align-items:flex-start;margin-bottom:2px}
.contact svg{flex:none;width:6px;height:6px;margin-top:1px}
.tagline{font-weight:700;text-transform:uppercase;line-height:1.6}
.tagline .hl{color:var(--orange)}
.slide-title{font-weight:700;font-size:9px;color:var(--navy);text-transform:uppercase}
.rule{width:16px;height:2px;background:var(--orange);margin-top:5px}
.slide-foot{position:absolute;left:10px;right:10px;bottom:4px;display:flex;justify-content:space-between;align-items:center;border-top:1px solid #ddd;padding-top:3px;font-size:4px;color:var(--muted)}
.slide-foot .brand{font-size:5px;gap:3px}
.slide-foot .mark{width:5px;height:5px}
.steps{position:absolute;display:flex;justify-content:space-between}
.step{display:flex;flex-direction:column;align-items:center;font-size:4.5px;text-align:center;color:var(--ink);width:42px;line-height:1.3}
.step .dot{width:18px;height:18px;border-radius:50%;border:1.2px solid var(--orange);margin-bottom:4px;display:flex;align-items:center;justify-content:center;background:#fff}
.step .dot svg{width:9px;height:9px}
.photo{position:absolute}
</style>
</head>
<body>

<!-- Letterhead -->
<section class="piece letterhead" style="left:19px;top:19px;width:372px;height:495px">
  <div class="brand" style="position:absolute;left:28px;top:40px;font-size:16px;gap:7px"><span class="mark" style="width:14px;height:14px"></span>VELTRONA</div>
  <div style="position:absolute;left:247px;top:33px;border-left:1px solid var(--orange);padding-left:10px;height:82px">
    <ul class="contact" style="font-size:5.2px">
      <li><svg viewBox="0 0 10 10"><path d="M2 1l2 2-1 1.5c.8 1.5 1.7 2.4 3 3L7.5 6l2 2-1.5 1.5C4 9 1 6 .5 1.5z" fill="var(--navy)"/></svg>+61 2 5550 0140</li>
      <li><svg viewBox="0 0 10 10"><rect x="0.5" y="2" width="9" height="6" fill="var(--navy)"/><path d="M.5 2l4.5 3.5L9.5 2" stroke="#fff" fill="none"/></svg>info@veltrona.com</li>
      <li><svg viewBox="0 0 10 10"><circle cx="5" cy="5" r="4.2" fill="none" stroke="var(--navy)"/><path d="M1 5h8M5 .8c-2 2.5-2 5.9 0 8.4M5 .8c2 2.5 2 5.9 0 8.4" stroke="var(--navy)" fill="none" stroke-width=".7"/></svg>www.veltrona.com</li>
      <li><svg viewBox="0 0 10 10"><path d="M5 .5a3.3 3.3 0 0 1 3.3 3.3C8.3 6.3 5 9.5 5 9.5S1.7 6.3 1.7 3.8A3.3 3.3 0 0 1 5 .5z" fill="var(--orange)"/></svg>Level 12, 48 Harbour Lane<br>Melbourne VIC 3000<br>Australia</li>
    </ul>
  </div>
  <div class="tagline" style="position:absolute;left:25px;top:428px;font-size:7.5px">Assurance.<br>Monitoring.<br><span class="hl">Delivering confidence.</span></div>
  <svg class="corner" width="170" height="128" viewBox="0 0 100 100" preserveAspectRatio="none"><polygon points="100,0 100,12 8,100 0,100" fill="var(--orange)"/><polygon points="100,14 100,100 11,100" fill="var(--navy)"/></svg>
</section>

<!-- Business card front -->
<section class="piece card-front" style="left:423px;top:17px;width:211px;height:127px">
  <div class="brand" style="position:absolute;left:15px;top:55px;font-size:11px;gap:6px"><span class="mark" style="width:11px;height:11px"></span>VELTRONA</div>
  <svg class="corner" width="85" height="76" viewBox="0 0 100 100" preserveAspectRatio="none"><polygon points="100,0 100,14 10,100 0,100" fill="var(--orange)"/><polygon points="100,16 100,100 13,100" fill="var(--navy)"/></svg>
</section>

<!-- Business card back -->
<section class="piece card-back" style="left:423px;top:160px;width:211px;height:117px">
  <div style="position:absolute;left:15px;top:16px">
    <div style="font-weight:700;font-size:8.5px;color:var(--navy)">DANIEL HARTLEY</div>
    <div style="font-size:5px;color:var(--orange);font-weight:600;margin-top:2px">MANAGING DIRECTOR</div>
  </div>
  <ul class="contact" style="position:absolute;left:15px;top:46px;font-size:5px">
    <li><svg viewBox="0 0 10 10"><path d="M2 1l2 2-1 1.5c.8 1.5 1.7 2.4 3 3L7.5 6l2 2-1.5 1.5C4 9 1 6 .5 1.5z" fill="var(--navy)"/></svg>+61 400 555 218</li>
    <li><svg viewBox="0 0 10 10"><rect x="0.5" y="2" width="9" height="6" fill="var(--navy)"/></svg>daniel.hartley@veltrona.com</li>
    <li><svg viewBox="0 0 10 10"><circle cx="5" cy="5" r="4.2" fill="none" stroke="var(--navy)"/></svg>www.veltrona.com</li>
    <li><svg viewBox="0 0 10 10"><path d="M5 .5a3.3 3.3 0 0 1 3.3 3.3C8.3 6.3 5 9.5 5 9.5S1.7 6.3 1.7 3.8A3.3 3.3 0 0 1 5 .5z" fill="var(--navy)"/></svg>Level 12, 48 Harbour Lane<br>Melbourne VIC 3000 Australia</li>
  </ul>
  <svg class="corner" width="78" height="96" viewBox="0 0 100 100" preserveAspectRatio="none"><polygon points="100,0 100,12 6,100 0,100" fill="var(--orange)"/><polygon points="100,14 100,100 10,100" fill="var(--navy)"/></svg>
</section>

<!-- Envelope -->
<section class="piece envelope" style="left:402px;top:294px;width:266px;height:124px">
  <div class="brand" style="position:absolute;left:18px;top:24px;font-size:8px"><span class="mark" style="width:9px;height:9px"></span>VELTRONA</div>
  <div style="position:absolute;left:18px;top:42px;font-size:3.8px;line-height:1.5;color:var(--muted)">Level 12, 48 Harbour Lane<br>Melbourne VIC 3000<br>Australia</div>
  <div style="position:absolute;left:19px;top:72px;width:107px;height:40px;border:1px solid #c9c9c9;border-radius:3px;background:#ebebeb"></div>
  <svg class="corner" width="86" height="68" viewBox="0 0 100 100" preserveAspectRatio="none"><polygon points="100,0 100,14 8,100 0,100" fill="var(--orange)"/><polygon points="100,16 100,100 12,100" fill="var(--navy)"/></svg>
</section>

<!-- Compliment slip -->
<section class="piece comp-slip" style="left:404px;top:430px;width:390px;height:83px">
  <div class="brand" style="position:absolute;left:18px;top:19px;font-size:8px"><span class="mark" style="width:9px;height:9px"></span>VELTRONA</div>
  <div style="position:absolute;left:119px;top:15px;height:20px;border-left:1px solid var(--orange)"></div>
  <div style="position:absolute;left:140px;top:22px;font-size:5.5px;font-weight:600;color:var(--navy)">With Compliments</div>
  <div style="position:absolute;left:0;right:0;top:62px;border-top:1px solid #ddd"></div>
  <ul class="contact" style="position:absolute;left:16px;top:67px;display:flex;gap:28px;font-size:4.8px">
    <li><svg viewBox="0 0 10 10"><path d="M2 1l2 2-1 1.5c.8 1.5 1.7 2.4 3 3L7.5 6l2 2-1.5 1.5C4 9 1 6 .5 1.5z" fill="var(--navy)"/></svg>+61 2 5550 0140</li>
    <li><svg viewBox="0 0 10 10"><rect x="0.5" y="2" width="9" height="6" fill="var(--navy)"/></svg>info@veltrona.com</li>
    <li><svg viewBox="0 0 10 10"><circle cx="5" cy="5" r="4.2" fill="none" stroke="var(--navy)"/></svg>www.veltrona.com</li>
  </ul>
  <svg class="corner" width="110" height="28" viewBox="0 0 100 100" preserveAspectRatio="none"><polygon points="100,0 100,12 5,100 0,100" fill="var(--orange)"/><polygon points="100,16 100,100 10,100" fill="var(--navy)"/></svg>
</section>

<!-- Presentation folder -->
<section class="piece folder" style="left:690px;top:23px;width:484px;height:328px;background:transparent">
  <div style="position:absolute;left:0;top:0;width:233px;height:328px;background:var(--navy)">
    <div class="brand light" style="position:absolute;left:24px;top:42px;font-size:10px"><span class="mark" style="width:10px;height:10px"></span>VELTRONA</div>
    <div class="tagline" style="position:absolute;left:24px;top:270px;font-size:6.2px;color:#fff">Assurance.<br>Monitoring.<br><span class="hl">Delivering confidence.</span></div>
  </div>
  <div style="position:absolute;left:233px;top:0;width:251px;height:328px;background:var(--paper)">
    <div class="brand" style="position:absolute;left:18px;top:42px;font-size:10px"><span class="mark" style="width:10px;height:10px"></span>VELTRONA</div>
    <svg class="corner" width="140" height="160" viewBox="0 0 100 100" preserveAspectRatio="none"><polygon points="100,0 100,10 8,100 0,100" fill="var(--orange)"/><polygon points="100,12 100,100 11,100" fill="var(--navy)"/></svg>
    <div style="position:absolute;left:0;top:240px;width:170px;height:88px;background:var(--navy-dark);clip-path:polygon(0 10%,8% 0,100% 0,100% 100%,0 100%)"></div>
    <div style="position:absolute;left:33px;top:271px;width:77px;height:38px;background:#fff;display:flex;align-items:center;justify-content:center"><span style="width:10px;height:10px;background:var(--orange)"></span></div>
  </div>
</section>

<!-- Capability prospectus -->
<section class="piece prospectus" style="left:839px;top:370px;width:317px;height:405px">
  <div class="brand" style="position:absolute;left:24px;top:42px;font-size:10.5px"><span class="mark" style="width:11px;height:11px"></span>VELTRONA</div>
  <div style="position:absolute;left:24px;top:100px">
    <div style="font-weight:700;font-size:17px;line-height:1.15;color:var(--navy)">CAPABILITY<br>PROSPECTUS</div>
    <div style="font-size:8px;line-height:1.6;color:var(--orange);margin-top:6px;font-weight:500">PROJECT ASSURANCE<br>&amp; MONITORING SOLUTIONS</div>
    <div style="font-size:7.5px;margin-top:5px">Across All Industries</div>
  </div>
  <svg class="corner" width="270" height="330" viewBox="0 0 100 100" preserveAspectRatio="none"><polygon points="100,0 100,6 4,100 0,100" fill="var(--orange)"/><polygon points="100,8 100,100 6,100" fill="var(--navy)"/></svg>
  <div class="tagline" style="position:absolute;left:204px;top:342px;font-size:6.2px;color:#fff">Assurance.<br>Monitoring.<br>Risk management.<br><span class="hl">Delivering confidence.</span></div>
</section>

<!-- Slide: cover -->
<section class="piece slide" style="left:20px;top:527px;width:273px;height:121px;background:var(--navy)">
  <div class="photo" role="img" aria-label="Two site engineers in hard hats and high-visibility vests looking at an industrial plant at sunset" style="right:0;top:0;width:165px;height:121px;background:linear-gradient(120deg,#e3a15a,#8a6a4d 55%,#3d4a4f);clip-path:polygon(42% 0,100% 0,100% 100%,0 100%)"></div>
  <svg style="position:absolute;left:108px;top:0" width="70" height="121" viewBox="0 0 100 100" preserveAspectRatio="none"><polygon points="100,0 96,0 0,100 5,100" fill="var(--orange)"/></svg>
  <div class="brand light" style="position:absolute;left:14px;top:20px;font-size:7px"><span class="mark" style="width:7px;height:7px"></span>VELTRONA</div>
  <div style="position:absolute;left:14px;top:66px;font-weight:700;font-size:8px;line-height:1.5;color:#fff"><span style="color:var(--orange)">DRIVING CONFIDENCE</span><br>IN EVERY PROJECT</div>
  <div style="position:absolute;left:14px;top:109px;font-size:4.5px;color:#fff;margin-top:-3px">Assurance. Monitoring. Excellence.</div>
</section>

<!-- Slide: who we are -->
<section class="piece slide" style="left:303px;top:527px;width:234px;height:121px">
  <div class="photo" role="img" aria-label="Modern glass office building against a blue sky" style="right:0;top:0;width:120px;height:108px;background:linear-gradient(160deg,#9bbcdc,#4f7aa6 60%,#2b4d74);clip-path:polygon(70% 0,100% 0,100% 100%,0 100%)"></div>
  <svg style="position:absolute;left:110px;top:0" width="86" height="108" viewBox="0 0 100 100" preserveAspectRatio="none"><polygon points="100,0 97,0 0,100 4,100" fill="var(--orange)"/></svg>
  <div style="position:absolute;left:13px;top:16px"><div class="slide-title">Who we are</div><div class="rule"></div></div>
  <p style="position:absolute;left:13px;top:45px;width:120px;font-size:4.8px;line-height:1.55;color:var(--muted)">Veltrona is a project assurance and monitoring company providing independent, objective and expert services to help organisations achieve successful outcomes.</p>
  <div class="slide-foot"><span class="brand"><span class="mark"></span>VELTRONA</span><span>02</span></div>
</section>

<!-- Slide: services -->
<section class="piece slide" style="left:548px;top:530px;width:245px;height:120px">
  <div style="position:absolute;left:15px;top:16px"><div class="slide-title">Our services</div><div class="rule"></div></div>
  <div style="position:absolute;left:32px;top:55px;width:182px;border-top:1px solid #cfd4db"></div>
  <div class="steps" style="left:11px;right:11px;top:46px">
    <div class="step"><span class="dot"><svg viewBox="0 0 10 10"><path d="M2 5l2 2 4-4" stroke="var(--navy)" fill="none" stroke-width="1.2"/></svg></span>Project<br>Assurance</div>
    <div class="step"><span class="dot"><svg viewBox="0 0 10 10"><circle cx="4.5" cy="4.5" r="3" stroke="var(--navy)" fill="none"/><path d="M7 7l2 2" stroke="var(--navy)"/></svg></span>Independent<br>Monitoring</div>
    <div class="step"><span class="dot"><svg viewBox="0 0 10 10"><path d="M5 1l4 8H1z" stroke="var(--navy)" fill="none"/></svg></span>Risk<br>Management</div>
    <div class="step"><span class="dot"><svg viewBox="0 0 10 10"><rect x="2" y="1.5" width="6" height="7" stroke="var(--navy)" fill="none"/><path d="M3.5 4h3M3.5 6h3" stroke="var(--navy)"/></svg></span>Compliance<br>&amp; Governance</div>
    <div class="step"><span class="dot"><svg viewBox="0 0 10 10"><path d="M2 8V6M4.5 8V4.5M7 8V2.5" stroke="var(--navy)" stroke-width="1.3"/></svg></span>Performance<br>Improvement</div>
  </div>
  <div class="slide-foot"><span class="brand"><span class="mark"></span>VELTRONA</span><span>06</span></div>
</section>

<!-- Slide: industries -->
<section class="piece slide" style="left:20px;top:659px;width:273px;height:121px">
  <div style="position:absolute;left:13px;top:16px"><div class="slide-title">Industries we serve</div><div class="rule"></div></div>
  <div class="steps" style="left:4px;right:4px;top:46px">
    <div class="step"><span class="dot" style="border:none;background:none"><svg viewBox="0 0 10 10"><path d="M3 9V2h2v7M1 9h8M6 9V5h2v4" stroke="var(--navy)" fill="none"/></svg></span>Oil &amp; Gas</div>
    <div class="step"><span class="dot" style="border:none;background:none"><svg viewBox="0 0 10 10"><rect x="1" y="3" width="7" height="3.5" stroke="var(--navy)" fill="none"/><circle cx="3" cy="8" r="1" stroke="var(--navy)" fill="none"/><circle cx="7" cy="8" r="1" stroke="var(--navy)" fill="none"/></svg></span>Mining</div>
    <div class="step"><span class="dot" style="border:none;background:none"><svg viewBox="0 0 10 10"><path d="M2 9V2h6v7M2 5h6M1 9h8" stroke="var(--navy)" fill="none"/></svg></span>Construction</div>
    <div class="step"><span class="dot" style="border:none;background:none"><svg viewBox="0 0 10 10"><path d="M1 9V5l4-3 4 3v4z" stroke="var(--navy)" fill="none"/></svg></span>Infrastructure</div>
    <div class="step"><span class="dot" style="border:none;background:none"><svg viewBox="0 0 10 10"><path d="M1 9V4l3 2V4l3 2V1h2v8z" stroke="var(--navy)" fill="none"/></svg></span>Manufacturing</div>
    <div class="step"><span class="dot" style="border:none;background:none"><svg viewBox="0 0 10 10"><path d="M6 1L2 6h3l-1 3 4-5H5z" stroke="var(--navy)" fill="none"/></svg></span>Energy</div>
    <div class="step"><span class="dot" style="border:none;background:none"><svg viewBox="0 0 10 10"><rect x="1" y="2" width="6" height="5" stroke="var(--navy)" fill="none"/><path d="M7 4h2v3H7" stroke="var(--navy)" fill="none"/></svg></span>Transport<br>&amp; Logistics</div>
  </div>
  <div class="slide-foot"><span class="brand"><span class="mark"></span>VELTRONA</span><span>07</span></div>
</section>

<!-- Slide: approach -->
<section class="piece slide" style="left:303px;top:659px;width:234px;height:121px">
  <div style="position:absolute;left:13px;top:16px"><div class="slide-title">Our approach</div><div class="rule"></div></div>
  <div class="steps" style="left:4px;right:4px;top:46px">
    <div class="step"><span class="dot" style="width:22px;height:22px;border-width:1.5px"><svg viewBox="0 0 10 10"><circle cx="5" cy="5" r="2.5" fill="var(--orange)"/></svg></span>Understand</div>
    <div class="step"><span class="dot" style="width:22px;height:22px;border-color:var(--navy);border-width:1.5px"><svg viewBox="0 0 10 10"><circle cx="4.5" cy="4.5" r="3" stroke="var(--navy)" fill="none"/><path d="M7 7l2 2" stroke="var(--navy)"/></svg></span>Assess</div>
    <div class="step"><span class="dot" style="width:22px;height:22px;border-width:1.5px"><svg viewBox="0 0 10 10"><path d="M2 5l2 2 4-4" stroke="var(--orange)" fill="none" stroke-width="1.3"/></svg></span>Assure</div>
    <div class="step"><span class="dot" style="width:22px;height:22px;border-color:var(--navy);border-width:1.5px"><svg viewBox="0 0 10 10"><path d="M1 6l2.5-2.5 2 2L9 2" stroke="var(--navy)" fill="none"/></svg></span>Monitor</div>
    <div class="step"><span class="dot" style="width:22px;height:22px;border-width:1.5px"><svg viewBox="0 0 10 10"><path d="M5 9V2M2 5l3-3 3 3" stroke="var(--orange)" fill="none"/></svg></span>Improve</div>
  </div>
  <svg style="position:absolute;left:0;top:62px" width="234" height="8" viewBox="0 0 234 8">
    <g stroke="var(--navy)" fill="var(--navy)"><path d="M38 4h10M82 4h10M126 4h10M170 4h10"/><polygon points="48,1 52,4 48,7"/><polygon points="92,1 96,4 92,7"/><polygon points="136,1 140,4 136,7"/><polygon points="180,1 184,4 180,7"/></g>
  </svg>
  <div class="slide-foot"><span class="brand"><span class="mark"></span>VELTRONA</span><span>08</span></div>
</section>

<!-- Slide: thank you -->
<section class="piece slide" style="left:548px;top:659px;width:245px;height:121px;background:var(--navy)">
  <div class="brand light" style="position:absolute;left:14px;top:20px;font-size:7px"><span class="mark" style="width:7px;height:7px"></span>VELTRONA</div>
  <div style="position:absolute;left:60px;top:48px;font-weight:700;font-size:16px;color:#fff;letter-spacing:.02em">THANK YOU</div>
  <div style="position:absolute;left:15px;top:100px;font-size:5px;color:#fff;display:flex;gap:5px;align-items:center"><svg width="6" height="6" viewBox="0 0 10 10"><circle cx="5" cy="5" r="4.2" fill="none" stroke="#fff"/></svg>www.veltrona.com</div>
  <svg class="corner" width="90" height="100" viewBox="0 0 100 100" preserveAspectRatio="none"><polygon points="100,0 100,12 6,100 0,100" fill="var(--orange)"/><polygon points="100,14 100,100 10,100" fill="var(--navy-dark)"/></svg>
</section>

</body>
</html>
```